Need brochure designed for my marijuana web startup.

PLEASE READ THE INSTRUCTIONS THOROUGHLY. YOUR SUBMISSION WILL BE REJECTED IF THEY ARE NOT FOLLOWED.

may lead to other immediate design work, such as flyers, postcards, banners, etc.

I need a PRINT trifold brochure or pamphlet designed for my company, Leafbrook.net. We are a bootstrapped medical marijuana search engine, locator, listing service and community.

I will be selling my web product and services to medical marijuana dispensaries and would like to quickly demonstrate why my service is better over my competitors..

I have drafted a (poorly designed) brochure that talks about all the points I wanted to hit on. I'd also like to add our 3 pricing plans in the brochure, but if there isn't any room, i'm fine with that.

I received some design guidelines from a branding consulting firm, so the designs must adhere to those rules. These guidelines are attached as a pdf. These guidelines include things like minimum clear space for the logo, primary and secondary colors, and font style.

Target Market(s)

marijuana dispensaries

Industry/Entity Type

Startup

Font styles to use
Other font styles liked:
• gotham rounded

Colors
9bcb3b

Requirements
Must have
• follow the design guidelines attached, including colors used! font files are attached.
• this is a PRINT brochure request. can be trifold, or 1 fold.
• The TEXT or "COPY" is all included in the brochure.doc attachment. There is additional stats in the "Nice to Haves" section that you may or may not include. up to you. Pricing info is included as an attachment called "Pricing Plan"
• please, keep it simple!
Nice to have
• some graphics.
• pricing plan.
• some statistics that may be interesting to help highlight how special unique items that are hard to find can be easily found with my service:
• From a sample of 2,594 active listings, there are over 153,000 items being sold:
• 12,900 marijuana related accessories (bongs, pipes, clothes, vapor pens, etc.)
• 20,300 concentrates
• 40,400 edibles
• 52,400 flowers (bud and shakes)
• 21,500 other - oral (pills, sprays), topical (lotions, soaps), seeds, oils
• 5,500 pre-rolled marijuana cigarettes (joints, blunts)
• of the 153,000 items, there are:
• 17,750+ hybrid items
• 27,100+ indica items
• 15,000+ sativa items
• in the world of edibles, there are:
• 200+ gluten free items
• 300+ sugar free items
• doses in edibles range from .3mg to 2,353mg (i.e. olive oil) the recommended dosage is 5-10mg
• 2,900+ items of 100mg edibles make it the most common dose offered on the market.
• there are over 4,000 items that are high in CBD (the medicinal chemical of weed).
Should not have
• no photos.

```html
<!DOCTYPE html>
<html lang="en">
<head>
<meta charset="utf-8">
<title>Leafbrook.net – Brochure</title>
<link href="https://fonts.googleapis.com/css2?family=Montserrat:wght@400;500;600;700&display=swap" rel="stylesheet">
<style>
  :root {
    --backdrop: #dcdcdc;
    --paper: #ffffff;
    --leaf: #8dc63f;
    --forest: #3b8f3c;
    --ink: #3a3a3a;
    --white: #ffffff;
  }
  * { margin: 0; padding: 0; box-sizing: border-box; }
  html, body { width: 1200px; height: 1000px; overflow: hidden; }
  body {
    background: var(--backdrop);
    font-family: "Montserrat", Arial, sans-serif;
    position: relative;
  }
  .sheet {
    position: absolute; left: 78px; top: 77px; width: 1053px; height: 817px;
    background: var(--paper);
    box-shadow: 14px 12px 18px rgba(0,0,0,0.12);
  }
  .benefits { position: absolute; left: 44px; top: 120px; width: 280px; }
  .benefits h2 { color: var(--leaf); font-size: 17px; font-weight: 700; margin-bottom: 12px; }
  .benefit { margin-bottom: 18px; }
  .benefit svg { display: block; margin-bottom: 4px; }
  .benefit p { font-size: 11px; line-height: 19px; color: var(--ink); }
  .coming-soon { position: absolute; left: 44px; top: 652px; }
  .coming-soon h3 { font-size: 11px; font-weight: 700; color: var(--forest); margin-bottom: 12px; }
  .coming-soon li { list-style: none; font-size: 11px; color: var(--forest); margin-bottom: 12px; }

  .cover { position: absolute; left: 391px; top: 45px; width: 623px; height: 549px; background: var(--leaf); }
  .contact { position: absolute; left: 23px; top: 270px; }
  .site { color: var(--white); font-size: 30px; font-weight: 500; margin-bottom: 18px; }
  .links li { list-style: none; color: var(--forest); font-size: 15px; font-weight: 500; line-height: 22px; }
  .message { position: absolute; left: 341px; top: 174px; width: 260px; }
  .headline { color: var(--white); font-size: 31px; font-weight: 500; line-height: 33px; margin-bottom: 20px; }
  .tagline { color: var(--forest); font-size: 15px; font-weight: 500; line-height: 22px; }
  .phone { position: absolute; left: 341px; top: 454px; display: flex; align-items: center; gap: 8px; color: var(--forest); font-size: 22px; font-weight: 500; }

  .brand { position: absolute; color: var(--forest); font-weight: 500; }
  .brand-stacked { left: 424px; top: 632px; width: 200px; display: flex; flex-direction: column; align-items: center; gap: 18px; font-size: 22px; }
  .brand-inline { left: 734px; top: 675px; display: flex; align-items: center; gap: 14px; font-size: 32px; }
  .brand-mark { border-radius: 50%; border: 3px solid var(--forest); }
  .brand-stacked .brand-mark { width: 62px; height: 62px; }
  .brand-inline .brand-mark { width: 62px; height: 62px; }
</style>
</head>
<body>
<main class="sheet">
  <section class="benefits">
    <h2>Benefits</h2>
    <div class="benefit">
      <svg width="42" height="34" viewBox="0 0 42 34" fill="none" stroke="var(--forest)" stroke-width="1.6">
        <rect x="1" y="1" width="40" height="26" rx="2"/>
        <line x1="1" y1="32" x2="41" y2="32" stroke-width="2.5"/>
        <path d="M10 20c-3-4-4-5-4-7a4 4 0 0 1 8 0c0 2-1 3-4 7z"/><circle cx="10" cy="13" r="1.4"/>
        <path d="M21 14c-3-4-4-5-4-7a4 4 0 0 1 8 0c0 2-1 3-4 7z"/><circle cx="21" cy="7" r="1.4"/>
        <path d="M32 20c-3-4-4-5-4-7a4 4 0 0 1 8 0c0 2-1 3-4 7z"/><circle cx="32" cy="13" r="1.4"/>
      </svg>
      <p>We do not manipulate search rankings<br>for the highest bidder.</p>
    </div>
    <div class="benefit">
      <svg width="26" height="32" viewBox="0 0 26 32" fill="none" stroke="var(--forest)" stroke-width="1.6">
        <path d="M13 31C5 21 2 17 2 12a11 11 0 0 1 22 0c0 5-3 9-11 19z"/><circle cx="13" cy="12" r="5"/>
      </svg>
      <p>Our map focuses on one listing at a time,<br>so your map marker always stands out and<br>is never obscured by other markers.</p>
    </div>
    <div class="benefit">
      <svg width="42" height="34" viewBox="0 0 42 34" fill="none" stroke="var(--forest)" stroke-width="1.6">
        <rect x="1" y="1" width="40" height="26" rx="2"/>
        <line x1="1" y1="32" x2="41" y2="32" stroke-width="2.5"/>
        <g stroke-width="2.4"><line x1="21" y1="7" x2="21" y2="20"/><line x1="15.5" y1="10" x2="26.5" y2="17"/><line x1="26.5" y1="10" x2="15.5" y2="17"/></g>
      </svg>
      <p>Our menus actually make sense.</p>
    </div>
    <div class="benefit">
      <svg width="34" height="30" viewBox="0 0 34 30" fill="none" stroke="var(--forest)" stroke-width="1.6">
        <path d="M17 2L32 28H2z" stroke-linejoin="round"/>
        <line x1="17" y1="10" x2="17" y2="19" stroke-width="2.4"/><circle cx="17" cy="23" r="1.2" fill="var(--forest)"/>
      </svg>
      <p>Users can follow your dispensary and items to<br>get instant alerts when you update things like<br>price and specials.</p>
    </div>
    <div class="benefit">
      <svg width="30" height="30" viewBox="0 0 30 30" fill="none" stroke="var(--forest)" stroke-width="1.6">
        <circle cx="15" cy="15" r="13.5"/>
        <path d="M19.5 10.5c-1-1.5-2.5-2-4.5-2-2.5 0-4 1.2-4 3 0 4.5 9 2.5 9 7 0 2-1.8 3.2-4.5 3.2-2.2 0-4-.8-5-2.4" stroke-width="2.2"/>
        <line x1="15" y1="5.5" x2="15" y2="24.5" stroke-width="2.2"/>
      </svg>
      <p>Most affordable service.</p>
    </div>
  </section>

  <section class="coming-soon">
    <h3>Coming soon...</h3>
    <ul>
      <li>Online Dispensary Registration</li>
      <li>Patient Verifications</li>
      <li>Online Ordering</li>
    </ul>
  </section>

  <section class="cover">
    <div class="contact">
      <p class="site">Leafbrook.net</p>
      <ul class="links">
        <li>friendspace.com/leafbrook</li>
        <li>chirper.com/leafbrook</li>
        <li>support@leafbrook.net</li>
      </ul>
    </div>
    <div class="message">
      <h1 class="headline">Finding weed shouldn’t be hard. We make it simple.</h1>
      <p class="tagline">Helping to make the<br>dispensary experience<br>simple.</p>
    </div>
    <div class="phone">
      <svg width="22" height="34" viewBox="0 0 22 34" fill="none" stroke="var(--forest)" stroke-width="1.6">
        <rect x="1" y="1" width="20" height="32" rx="3"/><rect x="4" y="5" width="14" height="20"/><circle cx="11" cy="29" r="1.5"/>
      </svg>
      <span>555.014.2290</span>
    </div>
  </section>

  <div class="brand brand-stacked"><span class="brand-mark"></span><span>leafbrook</span></div>
  <div class="brand brand-inline"><span class="brand-mark"></span><span>leafbrook</span></div>
</main>
</body>
</html>
```